Newly opened kids play space needs brochure to show what our space has to offer

Tri-fold color brochure with same aethetic as website (www.fernhollowplayhouse.com) that provides a comprehensive and visual overview of what our play space is comprised of. Features of the brochure should include our logo, "A Garrick and Pellinger-inspired Play Space in the Poconos", photos of: Dedicated Infant Play Area; Cafe and Free WiFi; Weekly Themed Activities; Unique Classes; Parties and Events. Photos also of our open play area with children playing within it. Info within the brochure should include our location, hours. Please take some copy from : https://www.facebook.com/fernhollowtinkerplayhouse/?ref=bookmarks
and from the Plan Your Visit part of the website. I have a lot of photos to use; is there a way to put in generic photo placeholders and I can pick which photos of mine to go into the various areas of the brochure, or if you need the photos ahead of time, please let me know the best way to proceed. I am attaching the logo files for now.

Font styles to use
Sans Serif

Colors
85cae6
cee9f5
86cfc6
cfeae6
fdf9cf
fff3d1
eaf2ce
cadf82

Requirements
Must have
• Eye catching placement of photos; color scheme similar to website and logo colors
Should not have
• Brochure should be simple, not too colorful - no primary colors, not too crowded.

```html
<!DOCTYPE html>
<html lang="en">
<head>
<meta charset="utf-8">
<title>Fern Hollow Play Space – Tri-fold Brochure</title>
<link rel="stylesheet" href="https://fonts.googleapis.com/css2?family=Ubuntu:wght@400;500;700&display=swap">
<style>
  :root {
    --backdrop: #a19fa7;
    --cream: #fbf8ea;
    --leaf: #c9df8a;
    --leaf-light: #dbeaa9;
    --ocean: #1f8dbf;
    --rose: #e8727f;
    --aqua: #86cfc6;
    --brown: #5a2a14;
    --brick: #b5301c;
    --ink: #1f1f1f;
    --coral: #ec7b61;
    --white: #ffffff;
  }
  * { box-sizing: border-box; margin: 0; padding: 0; }
  html, body { width: 1035px; height: 1200px; overflow: hidden; }
  body { background: var(--backdrop); font-family: "Ubuntu", sans-serif; color: var(--ink); position: relative; }

  .trim-mark { position: absolute; width: 0; border-left: 1px dashed #6f6d74; height: 26px; }

  .brochure-side { position: absolute; width: 696px; height: 538px; overflow: hidden;
    box-shadow: 3px 4px 8px rgba(0,0,0,.35); background: var(--cream); }
  .brochure-side.outside { left: 52px; top: 40px; }
  .brochure-side.inside { left: 283px; top: 613px; }
  .brochure-art { position: absolute; inset: 0; display: block; }

  .copy { position: absolute; white-space: nowrap; }
  .section-title { color: var(--brown); font-weight: 700; font-size: 18px; margin-bottom: 6px; }
  .section-body { font-size: 14px; line-height: 17px; color: var(--ink); }

  .hours-card { position: absolute; left: 273px; top: 78px; width: 165px; height: 237px;
    background: var(--white); border: 2px solid #e9e2cf; border-radius: 6px; text-align: center; padding-top: 30px; }
  .hours-title { color: var(--brown); font-weight: 700; font-size: 16px; margin-bottom: 8px; }
  .hours-days { color: var(--brick); font-size: 12px; }
  .hours-time { font-size: 11px; margin-bottom: 13px; margin-top: 2px; }

  .brand-name { position: absolute; font-family: "Ubuntu", sans-serif; font-weight: 700; white-space: nowrap; text-align: center; }
  .brand-name.cover { left: 464px; width: 232px; top: 62px; font-size: 32px; color: #2a8aa6; }
  .brand-name.footer { left: 232px; width: 232px; top: 418px; font-size: 30px; color: var(--white); }

  .contact { position: absolute; left: 232px; width: 232px; text-align: center; color: var(--white); }
  .contact .phone { position: absolute; top: 479px; width: 100%; font-weight: 700; font-size: 16px; }
  .contact .address { position: absolute; top: 498px; width: 100%; font-size: 9px; }
  .social-dots { position: absolute; top: 514px; left: 99px; display: flex; gap: 6px; }
  .social-dots span { width: 14px; height: 14px; border-radius: 2px; background: var(--white); opacity: .9; }

  .slogan { position: absolute; left: 464px; width: 232px; text-align: center; color: var(--white); }
  .slogan .headline { position: absolute; top: 423px; width: 100%; font-weight: 700; font-size: 20px; }
  .slogan .intro { position: absolute; top: 454px; width: 100%; font-size: 10.5px; line-height: 13px; }

  .web-pill { position: absolute; height: 24px; border-radius: 12px; background: var(--coral);
    border: 2px solid #f6b9a9; color: var(--white); font-size: 11px; display: flex; align-items: center;
    justify-content: center; gap: 5px; letter-spacing: .2px; white-space: nowrap; }
  .web-pill svg { width: 12px; height: 12px; flex: none; }
  .outside .web-pill { left: 502px; top: 500px; width: 160px; }
  .inside .web-pill { left: 258px; top: 498px; width: 160px; }
</style>
</head>
<body>
  <span class="trim-mark" style="left:285px;top:8px"></span>
  <span class="trim-mark" style="left:515px;top:8px"></span>
  <span class="trim-mark" style="left:515px;top:1160px"></span>
  <span class="trim-mark" style="left:745px;top:1160px"></span>

  <section class="brochure-side outside">
    <svg class="brochure-art" viewBox="0 0 696 538" xmlns="http://www.w3.org/2000/svg">
      <rect x="232" y="0" width="232" height="538" fill="var(--leaf)"/>
      <rect x="464" y="0" width="232" height="538" fill="var(--white)"/>
      <path d="M0,0 H300 C250,30 200,40 150,60 C100,85 50,98 0,98 Z" fill="var(--ocean)"/>
      <path role="img" aria-label="Photo: children and a parent playing at a table" d="M0,0 H285 C240,25 190,35 145,52 C95,72 50,85 0,85 Z" fill="#b9a690"/>
      <path d="M0,98 C50,98 100,85 150,60 C200,40 250,30 300,0 H310 C260,35 210,48 160,70 C110,95 55,108 0,108 Z" fill="var(--leaf-light)"/>
      <circle cx="188" cy="105" r="56" fill="var(--white)" stroke="var(--rose)" stroke-width="4"/>
      <circle role="img" aria-label="Photo: smiling girl with a toy" cx="188" cy="105" r="50" fill="#8b7d78"/>
      <rect role="img" aria-label="Photo: girl holding a woven craft on a wooden deck" x="464" y="128" width="232" height="270" fill="#8da173"/>
      <path d="M0,352 C140,320 300,385 440,378 C560,372 640,345 696,320 V538 H0 Z" fill="var(--leaf-light)"/>
      <path d="M0,370 C140,340 300,402 440,395 C560,389 640,362 696,340 V538 H0 Z" fill="var(--ocean)"/>
      <circle cx="113" cy="448" r="104" fill="var(--leaf)"/>
      <circle cx="113" cy="448" r="97" fill="var(--white)"/>
      <circle role="img" aria-label="Photo: girl sitting by a tree in the woods" cx="113" cy="448" r="92" fill="#8a6f55"/>
    </svg>

    <div class="copy" style="left:24px;top:168px">
      <h2 class="section-title">About Us</h2>
      <p class="section-body">Fern Hollow offers open-ended,<br>natural toys and activities<br>that nurture the child's<br>sense of wonder and invites<br>them to explore in our serene<br>and spacious environment.</p>
    </div>

    <div class="hours-card">
      <h3 class="hours-title">Open Play</h3>
      <p class="hours-days">Mon, Wed, Fri, Sun</p>
      <p class="hours-time">10:00AM - 5:00PM</p>
      <p class="hours-days">Tue, Thu, Sat</p>
      <p class="hours-time">10:00AM - 7:00PM</p>
      <h3 class="hours-title" style="margin-top:2px">Infants Only</h3>
      <p class="hours-days">Monday through Friday</p>
      <p class="hours-time">9:00AM - 10:00AM</p>
    </div>

    <div class="brand-name cover">Fern Hollow</div>
    <div class="brand-name footer">Fern Hollow</div>

    <div class="contact">
      <p class="phone">(272) 555-0147</p>
      <p class="address">42 Larkspur Lane, Stroudsburg, PA 18360</p>
      <div class="social-dots"><span></span><span></span></div>
    </div>

    <div class="slogan">
      <p class="headline">Play. Learn. Grow.</p>
      <p class="intro">We are a Garrick and<br>Pellinger-inspired play space<br>located in the <strong>Poconos</strong>.</p>
    </div>

    <a class="web-pill">
      <svg viewBox="0 0 12 12"><circle cx="6" cy="6" r="5" fill="none" stroke="#fff" stroke-width="1.2"/><path d="M1,6 H11 M6,1 C3,4 3,8 6,11 M6,1 C9,4 9,8 6,11" fill="none" stroke="#fff" stroke-width="1"/></svg>
      fernhollowplayhouse.com
    </a>
  </section>

  <section class="brochure-side inside">
    <svg class="brochure-art" viewBox="0 0 696 538" xmlns="http://www.w3.org/2000/svg">
      <rect x="232" y="0" width="232" height="538" fill="var(--leaf)"/>
      <path d="M0,128 C120,150 260,95 400,105 C520,115 600,120 696,105 V150 C600,165 520,150 400,140 C260,130 120,180 0,165 Z" fill="var(--ocean)"/>
      <path d="M0,160 C120,175 260,125 400,135 C520,145 600,155 696,140 V152 C600,168 520,158 400,148 C260,138 120,188 0,172 Z" fill="var(--leaf-light)"/>
      <path role="img" aria-label="Photo: parent and children crafting at a table" d="M0,0 H232 V120 C150,118 80,145 0,128 Z" fill="#b0a594"/>
      <path role="img" aria-label="Photo: parent with baby in the infant area" d="M232,0 H464 V104 C380,100 300,110 232,120 Z" fill="#a4908a"/>
      <path role="img" aria-label="Photo: children and families at a group class" d="M464,0 H696 V105 C600,120 520,115 464,106 Z" fill="#9d8a82"/>
      <circle cx="177" cy="177" r="69" fill="var(--white)" stroke="var(--rose)" stroke-width="4"/>
      <circle role="img" aria-label="Photo: parent enjoying coffee at the cafe" cx="177" cy="177" r="62" fill="#8c7466"/>
      <circle cx="465" cy="145" r="61" fill="var(--white)" stroke="var(--aqua)" stroke-width="4"/>
      <circle role="img" aria-label="Photo: toddler playing with a toy" cx="465" cy="145" r="55" fill="#9a8478"/>
      <circle cx="565" cy="162" r="46" fill="var(--white)" stroke="var(--ocean)" stroke-width="4"/>
      <circle role="img" aria-label="Photo: girl holding a craft" cx="565" cy="162" r="40" fill="#8e9c78"/>
      <path d="M0,470 C120,440 250,480 360,485 C470,490 600,500 696,470 V538 H0 Z" fill="var(--ocean)"/>
      <path d="M464,510 C560,500 640,470 696,455 V475 C640,490 560,515 464,520 Z" fill="var(--leaf)"/>
      <circle cx="140" cy="477" r="71" fill="var(--leaf)"/>
      <circle cx="140" cy="477" r="65" fill="var(--white)"/>
      <circle role="img" aria-label="Photo: smiling child painting" cx="140" cy="477" r="61" fill="#d9b04a"/>
      <circle cx="505" cy="460" r="84" fill="var(--ocean)"/>
      <circle cx="505" cy="460" r="79" fill="var(--white)"/>
      <circle role="img" aria-label="Photo: children at a themed party table" cx="505" cy="460" r="74" fill="#9b7f74"/>
    </svg>

    <div class="copy" style="left:30px;top:276px">
      <h2 class="section-title">Cafe and WIFI</h2>
      <p class="section-body">Take a break or catch up<br>on work while enjoying<br>Kettleworth coffee, beverages,<br>and healthy snacks.</p>
    </div>
    <div class="copy" style="left:255px;top:236px">
      <h2 class="section-title">Dedicated Infant Area</h2>
      <p class="section-body">Bond safely with your baby<br>while being within eyeshot<br>of the main play area.</p>
      <h2 class="section-title" style="margin-top:19px">Themed Activities</h2>
      <p class="section-body">Stories, crafts, and activities<br>change weekly to celebrate<br>the seasons and the world<br>around us.</p>
    </div>
    <div class="copy" style="left:489px;top:240px">
      <h2 class="section-title">Unique Classes</h2>
      <p class="section-body">Our multi-age, multi-sensory<br>approach to traditional classes<br>nurtures the whole child in a<br>creative and fun way.</p>
    </div>

    <a class="web-pill">
      <svg viewBox="0 0 12 12"><circle cx="6" cy="6" r="5" fill="none" stroke="#fff" stroke-width="1.2"/><path d="M1,6 H11 M6,1 C3,4 3,8 6,11 M6,1 C9,4 9,8 6,11" fill="none" stroke="#fff" stroke-width="1"/></svg>
      fernhollowplayhouse.com
    </a>
  </section>
</body>
</html>
```